Business and Success Coaching Business Card

Need a business card for my coaching business. I coach small businesses, career professionals and, individuals wanting to unlock their human potential and achieve excellence. At the heart of our methodology is the Shaping Purposeful Action Routines Knowingly (SPARK) approach to formulate empowerment, create principles for success and setting achievable outcomes. I would like something that incorporates our new logo, something clean and sharp with a solid darker, but complementary background, color on the card front. The back should be white where there will be room for three questions

Target Market(s)

People looking to advance and improve themselves through a success coach

Industry/Entity Type

Life Coaching

Contact Information for Business Card

Contact information on card.
Business name on front of card
Questions on back

Font styles to use
Other font styles liked:
• Century Gothic or other Serif style fonts that look similar to Century Gothic

Colors

Designer to choose colors to be used in the design.

Requirements
Must have
• Logo on front of card
• Business name - The Steady Forge
• Contact name - Ted Harlow
• Address - Box 4619, Ridgemoor, OR 97405-4619
• Phone number - 303-555-0147
• Email address - harlow.ted@thesteadyforge.example
• Certifications - ACC, CPC, MTC, NLPP
• Back of card
• Three questions on the back of the card:
• If you were at your best, what would you do right now?
• What is the decision you have been avoiding?
• What's one action you could take in the next 10 minutes?
Nice to have
• I would like to see a solid color on the front of the card that compliments the logo.
• Back should be white, or could be contrasting, but need to have the three questions.

```html
<!DOCTYPE html>
<html lang="en">
<head>
<meta charset="utf-8">
<title>The Steady Forge – Business Card</title>
<link href="https://fonts.googleapis.com/css2?family=Questrial&display=swap" rel="stylesheet">
<style>
  :root {
    --stage: #213a6e;
    --ink: #0a0d12;
    --paper: #ffffff;
    --accent: #4a86c8;
    --rule: #5a5f68;
  }
  * { box-sizing: border-box; margin: 0; padding: 0; }
  html, body { width: 1200px; height: 656px; overflow: hidden; }
  body {
    background: var(--stage);
    font-family: "Questrial", "Century Gothic", sans-serif;
    position: relative;
  }
  .card {
    position: absolute;
    top: 154px;
    width: 540px;
    height: 348px;
    overflow: hidden;
    box-shadow: 0 6px 18px rgba(0, 0, 0, 0.35);
  }
  .card--front { left: 40px; background: var(--ink); color: var(--paper); }
  .card--back { left: 620px; background: var(--paper); color: var(--ink); }

  /* Front */
  .brand {
    position: absolute;
    top: 76px;
    right: 22px;
    display: flex;
    align-items: center;
    gap: 8px;
  }
  .brand__dot { width: 12px; height: 12px; border-radius: 50%; background: var(--accent); }
  .brand__name { font-size: 14px; color: var(--accent); white-space: nowrap; }
  .holder {
    position: absolute;
    left: 16px;
    top: 196px;
    font-size: 35px;
    letter-spacing: 0.5px;
    font-weight: 400;
    white-space: nowrap;
  }
  .contact {
    position: absolute;
    left: 17px;
    right: 17px;
    top: 265px;
    height: 67px;
    border-top: 1px solid var(--rule);
    border-bottom: 1px solid var(--rule);
    display: grid;
    grid-template-columns: 253px 1fr;
  }
  .contact__col {
    display: flex;
    flex-direction: column;
    justify-content: center;
    gap: 10px;
    font-size: 11px;
    padding-left: 6px;
  }
  .contact__col + .contact__col { border-left: 1px solid var(--rule); padding-left: 38px; }
  .contact__item { display: flex; align-items: center; gap: 9px; white-space: nowrap; }
  .contact__icon { width: 12px; height: 12px; flex: none; }

  /* Back */
  .back-art { position: absolute; inset: 0; width: 100%; height: 100%; }
  .questions {
    position: absolute;
    left: 20px;
    top: 58px;
    list-style: none;
    display: flex;
    flex-direction: column;
    gap: 19px;
  }
  .question {
    position: relative;
    width: 367px;
    padding-left: 20px;
    padding-bottom: 4px;
    border-bottom: 1px solid var(--ink);
    font-size: 12.5px;
    white-space: nowrap;
  }
  .question::before {
    content: "";
    position: absolute;
    left: 0;
    bottom: -4px;
    width: 8px;
    height: 8px;
    background: var(--ink);
  }
  .question--spaced { letter-spacing: 1.4px; }
</style>
</head>
<body>
  <section class="card card--front" aria-label="Card front">
    <div class="brand">
      <span class="brand__dot"></span>
      <span class="brand__name">The Steady Forge</span>
    </div>
    <h1 class="holder">Ted Harlow</h1>
    <div class="contact">
      <div class="contact__col">
        <span class="contact__item">
          <svg class="contact__icon" viewBox="0 0 12 12"><path d="M6 0.5a4.3 4.3 0 0 0-4.3 4.3C1.7 8 6 11.5 6 11.5s4.3-3.5 4.3-6.7A4.3 4.3 0 0 0 6 0.5z" fill="#fff"/><circle cx="6" cy="4.8" r="1.6" fill="#0a0d12"/></svg>
          Box 4619, Ridgemoor, OR 97405-4619
        </span>
        <span class="contact__item">
          <svg class="contact__icon" viewBox="0 0 12 12"><rect x="2.5" y="0.5" width="7" height="11" rx="1" fill="#fff"/><rect x="3.5" y="1.8" width="5" height="7" fill="#0a0d12"/></svg>
          303-555-0147
        </span>
      </div>
      <div class="contact__col">
        <span class="contact__item">
          <svg class="contact__icon" viewBox="0 0 12 12"><rect x="0.5" y="2" width="11" height="8" fill="none" stroke="#fff"/><path d="M0.5 2L6 6.5 11.5 2M0.5 10L4.5 6M11.5 10L7.5 6" fill="none" stroke="#fff"/></svg>
          harlow.ted@thesteadyforge.example
        </span>
        <span class="contact__item">
          <svg class="contact__icon" viewBox="0 0 12 12"><path d="M6 2L0 5l6 3 6-3z" fill="#fff"/><path d="M2.5 6.5v2.5c0 1 7 1 7 0V6.5L6 8.3z" fill="#fff"/></svg>
          ACC, CPC, MTC, NLPP
        </span>
      </div>
    </div>
  </section>

  <section class="card card--back" aria-label="Card back">
    <svg class="back-art" viewBox="0 0 760 490" preserveAspectRatio="none" aria-hidden="true">
      <polygon points="0,262 638,490 0,490" fill="#0a0d12"/>
      <polygon points="658,0 760,0 760,490 480,490" fill="#4a86c8"/>
      <line x1="648" y1="0" x2="468" y2="432" stroke="#0a0d12" stroke-width="2"/>
    </svg>
    <ul class="questions">
      <li class="question">If you were at your best, what would you do right now?</li>
      <li class="question question--spaced">What is the decision you have been avoiding?</li>
      <li class="question">What’s one action you could take in the next 10 minutes?</li>
    </ul>
  </section>
</body>
</html>
```